Sports Team PP Investor Deck - Targeted to VCs

I need a designer touch to my PP deck ( investor presentation) All the content is there and core images just needs to look clean, modern/fresh and professional. The product is SquadHopper a youth sports team travel website. The presentation should look complementary to the look on the site ( SquadHopper.com) but no need match it. The colors should stay with in the color palette.
Logo colors:
Green 368C
Dark Blue 539C
Light Blue -306 C
Accents:
Cool Gray 8C
Orange 717C
Note page 3 will need 3 image to represent frustrations

Target Market(s)

VCs

Industry/Entity Type

Travel

Font styles to use
Sans Serif

Requirements
Must have
• Clean modern look, consistency in design, use cartoon images from our video that are provided

```html
<!DOCTYPE html>
<html lang="en">
<head>
<meta charset="utf-8">
<title>SquadHopper Investor Deck</title>
<link href="https://fonts.googleapis.com/css2?family=Lato:wght@300;400;700&display=swap" rel="stylesheet">
<style>
:root{
  --green:#7cc142;
  --navy:#1f3b57;
  --sky:#25a9e0;
  --gray:#8a8d8f;
  --orange:#f5821f;
  --red:#d8262b;
  --page:#ffffff;
  --slide-top:#ffffff;
  --slide-bottom:#e9eaeb;
  --text:#55595c;
}
*{box-sizing:border-box;margin:0;padding:0}
html,body{width:1200px;height:336px;overflow:hidden;background:var(--page);font-family:"Lato",sans-serif;color:var(--text)}
.deck{position:relative;width:1200px;height:336px}
.slide{position:absolute;width:186px;height:145px;background:linear-gradient(var(--slide-top),var(--slide-bottom));border:1px solid #d6d7d8;box-shadow:0 1px 2px rgba(0,0,0,.15);overflow:hidden}
.row1{top:3px}
.row2{top:180px}
.title{position:absolute;left:9px;top:7px;font-size:7px;color:var(--navy)}
.art{position:absolute;border-radius:3px}
.frame{position:absolute;border:1.5px solid var(--orange);border-radius:6px;background:#fff}
.issue{background:#fff;border:1px solid #ddd;margin-bottom:3px;padding:1.5px 2px;font-size:2.7px;line-height:1.3}
.label{position:absolute;left:6px;background:#fff;border:1px solid var(--green);border-left:3px solid var(--green);font-size:3.4px;color:var(--navy);padding:2px 3px;line-height:1.3}
.label em{font-style:italic;color:var(--green)}
.bullets{position:absolute;font-size:2.7px;line-height:1.45;color:var(--text);list-style:none}
.bullets li::before{content:"• ";color:var(--green)}
.brand{color:var(--navy)}
.brand.green{color:var(--green)}
.chip{display:block;height:12px}
</style>
</head>
<body>
<div class="deck">

<!-- Title -->
<section class="slide row1" style="left:5px">
  <div class="brand green" style="position:absolute;left:7px;top:6px;font-size:6px">SquadHopper</div>
  <div class="brand" style="position:absolute;left:0;width:186px;top:62px;text-align:center;font-size:14px">SquadHopper</div>
  <div style="position:absolute;left:0;width:186px;top:81px;text-align:center;font-size:5.5px;color:var(--gray)">Your Event Community</div>
</section>

<!-- Travel -->
<section class="slide row1" style="left:203px">
  <div class="title" style="font-size:6px">Teams Need to Travel. SquadHopper Makes it Simple.</div>
  <div class="frame" style="left:10px;top:20px;width:166px;height:116px"></div>
  <div class="art" role="img" aria-label="Cartoon of a coach, a player and a parent with a laptop planning team travel" style="left:16px;top:26px;width:154px;height:104px;background:linear-gradient(135deg,#e8eef5,#c9d9e8 50%,#f3dfc8)"></div>
</section>

<!-- Frustrations -->
<section class="slide row1" style="left:401px">
  <div class="title">Industry Frustrations</div>
  <div style="position:absolute;left:7px;top:19px;width:80px">
    <div class="issue">Fragmented team planning</div>
    <div class="issue">Very time consuming</div>
    <div class="issue">Inefficient and ineffective communication between members</div>
    <div class="issue">Teams need a one stop shop for travel and related activities</div>
    <div class="issue">Sports organizations need a simple way to manage team travel and events</div>
    <div class="issue">Businesses lack a way to reach traveling teams directly</div>
    <div class="issue">Time and energy lost. Revenue lost.</div>
  </div>
  <svg style="position:absolute;left:89px;top:20px" width="8" height="112" viewBox="0 0 8 112">
    <g stroke="var(--red)" stroke-width="1.6" stroke-linecap="round">
      <path d="M1 1l6 6M7 1l-6 6"/><path d="M1 12l6 6M7 12l-6 6"/><path d="M1 26l6 6M7 26l-6 6"/><path d="M1 42l6 6M7 42l-6 6"/><path d="M1 60l6 6M7 60l-6 6"/><path d="M1 78l6 6M7 78l-6 6"/><path d="M1 94l6 6M7 94l-6 6"/>
    </g>
  </svg>
  <div class="frame" style="left:102px;top:26px;width:78px;height:84px"></div>
  <div class="art" role="img" aria-label="Cartoons of a confused traveller, a bus and scattered plans" style="left:106px;top:30px;width:70px;height:76px;background:linear-gradient(160deg,#f6ead9,#e3c9a6)"></div>
</section>

<!-- Market players -->
<section class="slide row1" style="left:599px">
  <div class="title">Market players</div>
  <div class="art" role="img" aria-label="Cartoon of youth sports teams on a green field" style="left:7px;top:19px;width:82px;height:120px;background:linear-gradient(#cfe8b5,#7cc142)"></div>
  <div style="position:absolute;left:36px;top:126px;font-size:4.5px;color:var(--navy)">Teams</div>
  <div class="art" role="img" aria-label="Cartoon of hotels and restaurants" style="left:95px;top:19px;width:84px;height:52px;background:linear-gradient(#f2e3cf,#d9b88e)"></div>
  <div style="position:absolute;left:106px;top:60px;font-size:4.5px;color:#fff;background:var(--gray);padding:1px 3px">Businesses</div>
  <div class="art" role="img" aria-label="Cartoon of sports organization officials" style="left:95px;top:77px;width:84px;height:62px;background:linear-gradient(#e4edf5,#b8cfe3)"></div>
  <div style="position:absolute;left:100px;top:84px;font-size:4.5px;color:var(--navy);background:rgba(255,255,255,.85);padding:1px 3px">Sports Organizations</div>
</section>

<!-- Team travel transformed -->
<section class="slide row1" style="left:797px">
  <div class="title">Team Travel Transformed</div>
  <div class="art" role="img" aria-label="Cartoon of a team bus and hotel" style="left:9px;top:30px;width:40px;height:48px;background:linear-gradient(#f3e4cf,#dcb78a)"></div>
  <div class="art" role="img" aria-label="Cartoon of a stadium and players" style="left:137px;top:26px;width:40px;height:52px;background:linear-gradient(#e3edf6,#b9d0e4)"></div>
  <svg style="position:absolute;left:48px;top:36px" width="90" height="40" viewBox="0 0 90 40" fill="none" stroke="var(--sky)" stroke-width=".8">
    <path d="M2 6 L18 12"/><path d="M72 12 L88 6"/><path d="M2 34 L18 28"/><path d="M72 28 L88 34"/>
  </svg>
  <div class="brand green" style="position:absolute;left:52px;top:47px;font-size:8px;width:82px;text-align:center">SquadHopper</div>
  <div style="position:absolute;left:9px;top:106px;display:flex;gap:8px">
    <svg width="26" height="22" viewBox="0 0 24 22"><rect x=".5" y=".5" width="23" height="21" rx="2" fill="#fff" stroke="var(--sky)"/><path d="M6 8l5-2 6 2-1 8-5 1-4-3z" fill="var(--navy)"/></svg>
    <svg width="26" height="22" viewBox="0 0 24 22"><rect x=".5" y=".5" width="23" height="21" rx="2" fill="#fff" stroke="var(--sky)"/><path d="M5 9l7-4 7 4z M6 10h12v1H6z M7 11h1.5v6H7z M11 11h1.5v6H11z M15 11h1.5v6H15z M5 17h14v1.5H5z" fill="var(--navy)"/></svg>
    <svg width="26" height="22" viewBox="0 0 24 22"><rect x=".5" y=".5" width="23" height="21" rx="2" fill="#fff" stroke="var(--sky)"/><path d="M8 5l-4 3 2 3 2-1v8h8v-8l2 1 2-3-4-3-2 1h-4z" fill="var(--navy)"/></svg>
    <svg width="26" height="22" viewBox="0 0 24 22"><rect x=".5" y=".5" width="23" height="21" rx="2" fill="#fff" stroke="var(--sky)"/><path d="M5 14v-3l2-4h10l2 4v3z" fill="var(--navy)"/><circle cx="8" cy="15" r="1.5" fill="var(--navy)"/><circle cx="16" cy="15" r="1.5" fill="var(--navy)"/></svg>
    <svg width="26" height="22" viewBox="0 0 24 22"><rect x=".5" y=".5" width="23" height="21" rx="2" fill="#fff" stroke="var(--sky)"/><path d="M4 12l16-4-1 2-6 2-2 5h-2l1-4-5 1-1 1z" fill="var(--navy)"/></svg>
  </div>
</section>

<!-- Market size -->
<section class="slide row1" style="left:995px">
  <div class="title">Market Size</div>
  <div style="position:absolute;left:7px;top:19px;width:96px;height:120px;background:#fff;border:1px solid #e0e0e0">
    <ul class="bullets" style="left:3px;top:3px;width:90px;color:var(--sky)">
      <li>The youth sports travel industry is a multi billion dollar market</li>
      <li>SquadHopper immediate addressable market is sizable across the US</li>
      <li>Youth sports travel market</li>
      <li>High school and college events</li>
      <li>Thousands of teams in active market</li>
      <li>Millions of youth participants in club sports</li>
      <li>Millions of players on traveling teams</li>
      <li>Teams annually consume:</li>
      <li style="padding-left:4px">Hotel room nights</li>
      <li style="padding-left:4px">Restaurant meals</li>
      <li style="padding-left:4px">Car rentals and flights</li>
      <li style="padding-left:4px">Event and tournament fees</li>
      <li>Every team has a budget for travel and spends it each season</li>
    </ul>
  </div>
  <div class="art" role="img" aria-label="Cartoon of a cheering crowd of players and fans" style="left:108px;top:19px;width:71px;height:120px;background:linear-gradient(#dbe8f3,#9dbfdc 60%,#7cc142)"></div>
</section>

<!-- Traction -->
<section class="slide row2" style="left:5px">
  <div class="title">Traction &amp; Market validation</div>
  <div style="position:absolute;left:9px;top:16px;font-size:2.6px;color:var(--gray)">Ongoing milestones and validation</div>
  <div class="label" style="top:22px;width:38px">Customer validation</div>
  <div class="label" style="top:44px;width:38px">Signed Associations, Leagues and Tournaments</div>
  <div class="label" style="top:74px;width:38px">Signed National &amp; Regional Restaurant Chains</div>
  <div class="label" style="top:104px;width:38px">Featured in the following publications</div>
  <ul class="bullets" style="left:50px;top:22px;width:130px">
    <li>Successfully completed beta testing with teams and hotels</li>
    <li>Partnered with a regional youth soccer organization covering many clubs and thousands of teams</li>
    <li>Regional soccer league with several hundred teams signed</li>
    <li>Several tournaments signed for upcoming season</li>
    <li>Hotel groups and national chains onboarded</li>
    <li>Major hotel brands and regional hotel operators</li>
    <li>National restaurant partners across several cuisines and family chains</li>
  </ul>
  <div style="position:absolute;left:50px;top:110px;display:flex;gap:6px">
    <span class="chip" style="width:28px;background:#d8e7f2"></span>
    <span class="chip" style="width:24px;background:#cfd3d6"></span>
    <span class="chip" style="width:30px;background:#e8c7c2"></span>
    <span class="chip" style="width:16px;background:#f4dc7a"></span>
  </div>
</section>

<!-- Growth charts -->
<section class="slide row2" style="left:203px">
  <div class="title">Addressable Events, Teams and Members Growth</div>
  <svg style="position:absolute;left:8px;top:19px" width="82" height="60" viewBox="0 0 74 60" preserveAspectRatio="none">
    <rect x=".5" y=".5" width="73" height="59" fill="#fff" stroke="#ccc"/>
    <text x="37" y="7" font-size="3.6" text-anchor="middle" fill="#55595c" font-family="Lato,sans-serif">Teams by Quarters</text>
    <g fill="#f5821f"><rect x="12" y="48" width="6" height="2"/><rect x="24" y="42" width="6" height="8"/><rect x="36" y="32" width="6" height="18"/><rect x="48" y="22" width="6" height="28"/><rect x="60" y="12" width="6" height="38"/></g>
    <path d="M8 50h62M8 10v40" stroke="#bbb" stroke-width=".4"/>
  </svg>
  <svg style="position:absolute;left:96px;top:19px" width="82" height="60" viewBox="0 0 74 60" preserveAspectRatio="none">
    <rect x=".5" y=".5" width="73" height="59" fill="#fff" stroke="#ccc"/>
    <text x="37" y="7" font-size="3.6" text-anchor="middle" fill="#55595c" font-family="Lato,sans-serif">Members by Quarters</text>
    <g fill="#f5821f"><rect x="12" y="48" width="6" height="2"/><rect x="24" y="44" width="6" height="6"/><rect x="36" y="36" width="6" height="14"/><rect x="48" y="24" width="6" height="26"/><rect x="60" y="12" width="6" height="38"/></g>
    <path d="M8 50h62M8 10v40" stroke="#bbb" stroke-width=".4"/>
  </svg>
  <svg style="position:absolute;left:36px;top:85px" width="114" height="54" viewBox="0 0 104 54" preserveAspectRatio="none">
    <rect x=".5" y=".5" width="103" height="53" fill="#fff" stroke="#ccc"/>
    <text x="52" y="7" font-size="3.6" text-anchor="middle" fill="#55595c" font-family="Lato,sans-serif">Total Sporting Events to Date</text>
    <g fill="#f5821f"><rect x="16" y="40" width="8" height="6"/><rect x="32" y="32" width="8" height="14"/><rect x="48" y="22" width="8" height="24"/><rect x="64" y="14" width="8" height="32"/></g>
    <path d="M10 46h72M10 10v36" stroke="#bbb" stroke-width=".4"/>
    <rect x="84" y="16" width="3" height="3" fill="#f5821f"/><text x="88" y="19" font-size="2.4" fill="#55595c" font-family="Lato,sans-serif">Events</text>
  </svg>
</section>

<!-- Revenue model -->
<section class="slide row2" style="left:401px">
  <div class="title">Revenue Model</div>
  <div class="label" style="top:30px;width:52px">Teams –<br><em>Commission and Transaction Model</em></div>
  <div class="label" style="top:70px;width:52px">Business –<br><em>Fee Based and Commission Model</em></div>
  <div class="label" style="top:100px;width:52px">Sports Organizations –<br><em>Fee Based and Commission Model</em></div>
  <ul class="bullets" style="left:64px;top:24px;width:116px;font-size:3.2px">
    <li>Multiple revenue opportunities to fill team needs</li>
    <li>Currently: hotel nights, restaurant reservations (dine-in and pick-up)</li>
    <li>In development: merchandise, activities, ground transportation</li>
    <li>Future: vertical markets non-sports groups</li>
  </ul>
  <ul class="bullets" style="left:64px;top:72px;width:116px;font-size:3.2px"><li>Advertising, premium placement, professional and premier levels</li></ul>
  <ul class="bullets" style="left:64px;top:102px;width:116px;font-size:3.2px"><li>Data mining</li><li>Event promotion opportunities</li></ul>
</section>

<!-- Team -->
<section class="slide row2" style="left:599px">
  <div class="title">Team</div>
  <div class="label" style="top:22px;width:36px;height:38px;padding-top:15px">Management</div>
  <div class="label" style="top:66px;width:36px;height:38px;padding-top:13px">Board of Advisors</div>
  <div class="label" style="top:110px;width:36px;height:26px;padding-top:10px">Support</div>
  <ul class="bullets" style="left:48px;top:22px;width:132px">
    <li>Marco Delane, CEO – software executive, soccer coach</li>
    <li>Nora Vell, VP Marketing – founder, sports marketing</li>
    <li>Evan Rourke, VP Engineering – aerospace engineer</li>
    <li>Sami Kord, CTO – platform architect</li>
    <li>Owen Pratt, Corporate Development – former soccer executive</li>
  </ul>
  <ul class="bullets" style="left:48px;top:68px;width:132px">
    <li>Jordan Keel – sports analyst, former national team player</li>
    <li>Reid Cassin – former director of clubs</li>
    <li>Lou Harbin – former VP Engineering</li>
    <li>Glen Osterby – President, venture firm</li>
  </ul>
  <ul class="bullets" style="left:48px;top:114px;width:132px">
    <li>Law Firm – Harlow &amp; Finch LLP</li>
    <li>Accounting Firm – Brightmark CPAs</li>
  </ul>
</section>

<!-- Accelerating growth -->
<section class="slide row2" style="left:797px">
  <div class="title">Accelerating Growth</div>
  <div style="position:absolute;left:9px;top:18px;width:170px;font-size:3px;color:var(--navy);line-height:1.4">Increase the number of teams in SquadHopper and create more spending opportunities by continuing to build out:</div>
  <div class="label" style="top:34px;width:38px;height:26px;padding-top:9px">Partnerships</div>
  <div class="label" style="top:70px;width:38px;height:28px;padding-top:7px">Product development</div>
  <div class="label" style="top:108px;width:38px">Staffing</div>
  <ul class="bullets" style="left:50px;top:36px;width:130px;font-size:3px">
    <li>Access sports organization companies to expedite onboarding</li>
    <li>Continue to add national hotel and restaurant chains</li>
    <li>Build relationships with other event related service providers</li>
  </ul>
  <ul class="bullets" style="left:50px;top:72px;width:130px;font-size:3px">
    <li>Continue to refine systems</li>
    <li>Add new features and revenue for enhanced customer satisfaction</li>
    <li>Add more revenue producing modules</li>
  </ul>
  <ul class="bullets" style="left:50px;top:109px;width:130px;font-size:3px"><li>Increasing influential industry sales staff</li></ul>
</section>

<!-- Thank you -->
<section class="slide row2" style="left:995px">
  <div style="position:absolute;left:0;width:186px;top:36px;text-align:center;font-size:18px;color:var(--navy);font-weight:300">Thank you</div>
  <div class="brand green" style="position:absolute;left:0;width:186px;top:80px;text-align:center;font-size:13px">SquadHopper</div>
</section>

</div>
</body>
</html>
```